Book Cover Design Book About Commercial Real Estate Investing

I need a book cover designed for my upcoming book.
Need cover for paperback and hardcover book.

The Book is about investing in net lease commercial property.

The book title:

The Steady Yield Manual
Proven Methods For Passive Landlord Buyers
By Mara Colby

Should be minimalist, clean, authoritative, convey money, trust, & growth
I think I like the colors white red and black.
I want a front cover at this time.

Samples I like are included. - the red white and blacks are my favorites

My company is The Corlane Circle
you can learn more about Triple Net Properties at my website
www.TheCorlaneCircle.com

the symbol NNN = Triple net in commercial real estate

Target Market(s)

Affluent male conservative investors

Industry/Entity Type

Real Estate

Requirements
Nice to have
• Sports Motif - - diagrams of sports plays from playbook
• google - Diagrams of sports plays -

```html
<!DOCTYPE html>
<html lang="en">
<head>
<meta charset="utf-8">
<title>The Steady Yield Manual — Cover</title>
<link rel="stylesheet" href="https://fonts.googleapis.com/css2?family=Saira+Condensed:wght@500;600&family=Roboto+Slab:wght@700&family=Roboto+Condensed:wght@700&family=Tinos&family=Roboto:wght@400&display=swap">
<style>
  :root {
    --sky: #2490cb;
    --paper: #ffffff;
    --indigo: #3a4fa6;
    --ice: #5cb6e8;
    --steel: #2c62a4;
    --deep: #2a64a2;
    --ink: #2f3d98;
    --spine-dark: #2e3b8c;
    --spine-mid: #2a5b9c;
  }
  * { margin: 0; padding: 0; box-sizing: border-box; }
  html, body { width: 1079px; height: 1200px; overflow: hidden; background: var(--paper); }
  .cover { position: relative; width: 1079px; height: 1200px; overflow: hidden; background: var(--paper); }

  .band-top { position: absolute; left: 0; top: 0; width: 100%; height: 634px; background: var(--sky); }
  .band-bottom { position: absolute; left: 0; top: 1114px; width: 100%; height: 86px; background: var(--sky); }

  .spine-shade { position: absolute; left: 0; width: 146px; }
  .spine-shade.on-blue { top: 0; height: 634px; background: linear-gradient(to right, rgba(255,255,255,.14), rgba(255,255,255,.22) 85%, rgba(255,255,255,.05)); }
  .spine-shade.on-white { top: 634px; height: 480px; background: linear-gradient(to right, rgba(0,0,0,.03), rgba(0,0,0,.08) 85%, rgba(0,0,0,.02)); }
  .spine-shade.on-base { top: 1114px; height: 86px; background: rgba(255,255,255,.08); }

  .spine-title {
    position: absolute; left: 22px; bottom: 76px;
    writing-mode: vertical-rl; transform: rotate(180deg);
    font-family: "Saira Condensed", sans-serif; font-weight: 600;
    font-size: 84px; line-height: 1; letter-spacing: 2px; white-space: nowrap;
    color: var(--spine-dark);
  }
  .spine-title .accent { color: var(--ice); }
  .spine-title .tail { color: var(--spine-mid); }

  .title {
    position: absolute; right: 22px; top: 262px; text-align: right;
    font-family: "Saira Condensed", sans-serif; font-weight: 500; line-height: 1;
  }
  .title .line-one { display: block; font-size: 128px; letter-spacing: 6px; color: var(--steel); }
  .title .line-one .lead { color: var(--indigo); }
  .title .line-one .accent { color: var(--ice); }
  .title .line-two { display: block; margin-top: 22px; font-size: 170px; letter-spacing: 10px; color: var(--deep); }

  .subtitle {
    position: absolute; right: 46px; top: 680px; text-align: right;
    font-family: "Roboto Condensed", "Roboto Slab", serif; font-weight: 700;
    font-size: 50px; line-height: 64px; letter-spacing: 2px; color: var(--ink);
  }
  .author {
    position: absolute; right: 44px; top: 1010px;
    font-family: "Roboto Condensed", serif; font-weight: 700;
    font-size: 52px; letter-spacing: 2px; color: var(--sky);
  }
  .year {
    position: absolute; left: 18px; top: 1130px;
    font-family: "Tinos", serif; font-size: 42px; color: var(--ink);
  }
  .site {
    position: absolute; right: 30px; top: 1142px;
    font-family: "Roboto", sans-serif; font-size: 21px; color: var(--ink);
  }
</style>
</head>
<body>
<main class="cover">
  <div class="band-top"></div>
  <div class="band-bottom"></div>
  <div class="spine-shade on-blue"></div>
  <div class="spine-shade on-white"></div>
  <div class="spine-shade on-base"></div>

  <div class="spine-title">THE <span class="accent">STEADY</span> YIELD<span class="tail">MANUAL</span></div>

  <h1 class="title">
    <span class="line-one"><span class="lead">THE</span> <span class="accent">STEADY</span> YIELD</span>
    <span class="line-two">MANUAL</span>
  </h1>

  <p class="subtitle">Proven Methods For Passive<br>Landlord Buyers.</p>
  <p class="author">By Mara Colby</p>

  <p class="year">2002</p>
  <p class="site">www.TheCorlaneCircle.com</p>
</main>
</body>
</html>
```